依頼詳細
商品名は「霧峰ミルク石鹸」で
補足文として商品名の前に「霧峰温泉生まれの」、
商品名の近くに「KIRIMINE-MILK-SOAP」もしくは「KIRIMINE MILK SOAP」の
英名を付記してください。

パッケージは大中小の3サイズで、
3つとも共通デザインでも結構ですし、
色違いでご提案いただいても結構です。

パッケージ表面にサイズがわかるよう
大、レギュラー、regular
中、ミドル、middle
小、ミニ、mini
上のひらがな、漢字、アルファベットのいずれかの表示をお願いします。

記載項目
パッケージの形状およびサイズは添付のデータをご確認ください。
希望イメージ
シンプル 複雑
単色 カラフル
暗い 明るい
日常 高級
遊び心 厳粛
未来的 伝統的
女性的 男性的
希望する色
茶系、緑系
納品ファイル
• イラストレーター形式 (.ai)
補足説明

```html
<!DOCTYPE html>
<html lang="ja">
<head>
<meta charset="utf-8">
<title>霧峰ミルク石鹸 ピローボックス展開図 regular</title>
<link rel="stylesheet" href="https://fonts.googleapis.com/css2?family=Shippori+Mincho:wght@500;700&family=Cormorant+Garamond:wght@500&family=Quicksand:wght@500&display=swap">
<style>
  :root {
    --paper: #ffffff;
    --dieline: #2b2b2b;
    --kraft: #c9ab7d;
    --kraft-deep: #b8966a;
    --mist-blue: #c4e2e6;
    --label: #ffffff;
    --olive: #6a6830;
    --olive-soft: #8a874a;
    --ink: #4a4636;
  }
  * { margin: 0; padding: 0; box-sizing: border-box; }
  html, body { width: 891px; height: 1200px; overflow: hidden; background: var(--paper); }
  .dieline-sheet { position: relative; width: 891px; height: 1200px; }
  .dieline-art { position: absolute; inset: 0; }
  .size-mark {
    position: absolute; left: 655px; top: 262px;
    font-family: "Quicksand", sans-serif; font-size: 19px; color: var(--ink);
  }
  .product-label {
    position: absolute; left: 409px; top: 340px; width: 280px;
    text-align: center; color: var(--olive);
  }
  .product-origin {
    font-family: "Shippori Mincho", serif; font-weight: 500;
    font-size: 14px; letter-spacing: 1px; color: var(--olive-soft);
  }
  .product-name {
    font-family: "Shippori Mincho", serif; font-weight: 700;
    font-size: 33px; letter-spacing: 1px; margin-top: 4px; line-height: 1.2;
  }
  .product-name-en {
    font-family: "Cormorant Garamond", serif; font-weight: 500;
    font-size: 17px; letter-spacing: 3px; margin-top: 18px;
  }
</style>
</head>
<body>
<main class="dieline-sheet">
  <svg class="dieline-art" width="891" height="1200" viewBox="0 0 891 1200" aria-hidden="false">
    <defs>
      <clipPath id="front-panel-clip">
        <path d="M238,54 L748,54 Q688,372 748,690 L238,690 Q298,372 238,54 Z"/>
      </clipPath>
    </defs>

    <!-- die cut outline -->
    <path class="cut-line" fill="var(--paper)" stroke="var(--dieline)" stroke-width="1.6"
      d="M238,54 L748,54
         C820,110 860,200 860,330 A35,35 0 0 0 860,400
         C860,520 820,640 748,690
         C820,740 860,800 860,880 A35,35 0 0 0 860,950
         C860,1040 820,1090 748,1123
         L238,1123
         C166,1090 126,1040 126,950 A35,35 0 0 0 126,880
         C126,800 166,740 238,690
         C166,640 126,520 126,400 A35,35 0 0 0 126,330
         C126,200 166,110 238,54 Z"/>

    <!-- front panel -->
    <path class="front-panel" fill="var(--kraft)"
      d="M238,54 L748,54 Q688,372 748,690 L238,690 Q298,372 238,54 Z"/>
    <g clip-path="url(#front-panel-clip)">
      <path class="pattern-area" role="img" aria-label="水色の地に黒い短い線が散る装飾模様"
        fill="var(--mist-blue)"
        d="M230,54 H455 C395,110 320,150 330,250 C338,330 290,420 262,530 L230,530 Z"/>
      <path class="pattern-area" role="img" aria-label="茶色の地に黒い丸点が並ぶ装飾模様"
        fill="var(--kraft-deep)"
        d="M230,545 C300,520 390,570 430,690 L230,690 Z"/>
    </g>

    <!-- back panel -->
    <path class="back-panel" fill="var(--kraft)"
      d="M238,690 L748,690 Q688,906 748,1123 L238,1123 Q298,906 238,690 Z"/>

    <!-- fold line -->
    <line class="fold-line" x1="238" y1="690" x2="748" y2="690" stroke="var(--dieline)" stroke-width="1"/>

    <!-- scalloped label -->
    <g class="label-badge" fill="var(--label)">
      <circle cx="549" cy="416" r="112"/>
      <circle cx="549" cy="302" r="34"/>
      <circle cx="616" cy="324" r="34"/>
      <circle cx="657" cy="381" r="34"/>
      <circle cx="657" cy="451" r="34"/>
      <circle cx="616" cy="508" r="34"/>
      <circle cx="549" cy="530" r="34"/>
      <circle cx="482" cy="508" r="34"/>
      <circle cx="441" cy="451" r="34"/>
      <circle cx="441" cy="381" r="34"/>
      <circle cx="482" cy="324" r="34"/>
    </g>
  </svg>

  <p class="size-mark">regular</p>

  <div class="product-label">
    <p class="product-origin">霧峰温泉生まれの</p>
    <h1 class="product-name">霧峰ミルク石鹸</h1>
    <p class="product-name-en">KIRIMINE MILK SOAP</p>
  </div>
</main>
</body>
</html>
```